Business card - Kite Harbor - size 85 mm * 55 mm

We need new business cards. Design must fit with our vision of the firm. You find in the attached file our logo and a short description of our firm (mission, vision, value, business and so on).

Target Market(s)

Consulting firm in performance improvement

Industry/Entity Type

Management Consulting

Contact Information for Business Card

SIZE
85 mm * 55 mm
INFORMATIONS
name surname
role position
telephone number
email address

Requirements
Must have
• the brand must APPEAR for the rest Would we like to have something sleek, inspired to a "just right" approach
Should not have
• Please avoid the black color as background

```html
<!DOCTYPE html>
<html lang="en">
<head>
<meta charset="utf-8">
<title>Kite Harbor – Business Card</title>
<link rel="stylesheet" href="https://fonts.googleapis.com/css2?family=Arimo:wght@400;700&display=swap">
<style>
  :root {
    --brand-orange: #ff6600;
    --accent-green: #9fcaa6;
    --card-white: #ffffff;
    --text-grey: #555555;
    --rule-grey: #8a8a8a;
    --page-bg: #e6e6e6;
  }
  * { box-sizing: border-box; margin: 0; padding: 0; }
  html, body {
    width: 1105px;
    height: 1200px;
    overflow: hidden;
  }
  body {
    background: var(--page-bg);
    font-family: "Arimo", Arial, sans-serif;
    position: relative;
  }
  .card {
    position: absolute;
    left: 217px;
    width: 688px;
    height: 445px;
    overflow: hidden;
  }
  .card-front { top: 135px; background: var(--card-white); }
  .card-back  { top: 627px; background: var(--brand-orange); }

  .front-swoosh {
    position: absolute;
    top: 0; left: 0;
    width: 688px; height: 445px;
  }

  .brand-mark {
    position: absolute;
    border-radius: 50%;
  }
  .card-front .brand-mark {
    left: 428px; top: 44px;
    width: 132px; height: 132px;
    border: 5px solid var(--brand-orange);
  }
  .card-back .brand-mark {
    left: 256px; top: 108px;
    width: 160px; height: 160px;
    border: 6px solid var(--card-white);
  }

  .brand-name {
    position: absolute;
    font-weight: 400;
    text-transform: uppercase;
    white-space: nowrap;
    text-align: center;
  }
  .card-front .brand-name {
    left: 330px; top: 187px;
    width: 350px;
    font-size: 20px;
    letter-spacing: 6px;
    color: var(--brand-orange);
  }
  .card-back .brand-name {
    left: 94px; top: 290px;
    width: 500px;
    font-size: 28px;
    letter-spacing: 9px;
    color: var(--card-white);
  }

  .holder {
    position: absolute;
    left: 43px; top: 330px;
    white-space: nowrap;
  }
  .holder-name {
    font-size: 24px;
    font-weight: 700;
    color: var(--brand-orange);
  }
  .holder-role {
    font-size: 19px;
    color: var(--text-grey);
  }
  .holder-role .dash {
    color: var(--brand-orange);
    font-weight: 700;
  }
  .divider {
    position: absolute;
    left: 43px; top: 370px;
    width: 587px; height: 1px;
    background: var(--rule-grey);
  }
  .contact-line {
    position: absolute;
    left: 43px; top: 381px;
    font-size: 17px;
    color: var(--text-grey);
    white-space: nowrap;
  }
  .contact-line .label {
    color: var(--brand-orange);
    margin-right: 4px;
  }
  .contact-line .item { margin-right: 10px; }
</style>
</head>
<body>
  <section class="card card-front" aria-label="Business card front">
    <svg class="front-swoosh" viewBox="0 0 688 445" aria-hidden="true">
      <path d="M0 0 H470 C300 22 90 80 0 186 Z" fill="var(--accent-green)"/>
      <path d="M0 0 H470 C290 14 80 60 0 152 Z" fill="var(--brand-orange)"/>
    </svg>
    <div class="brand-mark" aria-hidden="true"></div>
    <div class="brand-name">Kite Harbor</div>

    <div class="holder">
      <span class="holder-name">Elena Marsh</span>
      <span class="holder-role"><span class="dash">-</span> President</span>
    </div>
    <div class="divider"></div>
    <div class="contact-line">
      <span class="item"><span class="label">P :</span>555 0142 7788</span>
      <span class="item"><span class="label">E :</span>hello@kiteharbor.com</span>
      <span class="item"><span class="label">W :</span>www.kiteharbor.com</span>
    </div>
  </section>

  <section class="card card-back" aria-label="Business card back">
    <div class="brand-mark" aria-hidden="true"></div>
    <div class="brand-name">Kite Harbor</div>
  </section>
</body>
</html>
```